Academic acomlishments and book promotional business card

Must Present my accomplishments in a strong fashion while looking very professional. We will need to make last minute changes in book title in about one to two months so it can't close until then. Must place a great emphasis on peer review. Treat this as if it were my business. It is more important than my titles. Vary fond slightly to emphasize peer review.

Reason: I will need to make small changes in book title in a month or two so it can't close until then.

Target Market(s)

Scholars, employers, patrons, and professionals.

Industry/Entity Type

Business

Contact Information for Business Card

Basic content:

Grant T. Vellimore
Peer review by: Harwick Scholarly Press + Marten Books + R. J. Fallow Co. + Peter Quade & Sons

Evolutionary Scientist + Historian

Academic Consultant, Ellsworth Academic Press

See Overleaf

grantvell@mailbrook.net + Cell. (555) 214-0873

Reverse Side:

In the distant future I see open fields for far more important researches. Psychology will be based on a new foundation, that of the necessary squire Kent of each mental power by gradation. Light will be thrown on the origin of man and his history. --Edmund Farrow [make dash one line]

Book: "Moral Roots or Civic Roots: Adaptive Behaviour,..."

See Friendlane for CV with Endorsements + Writing Sample.

Font styles to use
Serif

Requirements
Must have
• The font has to be big enough etc to be able to use the gold ink at prindo.com, who will print them. Pls see their website for specs.
Nice to have
• Have a capital of the last letter in the Greek alphabet as a decorative element. Though this is not necessary.
Should not have
• Not Ornate or very curvalinear font.

```html
<!DOCTYPE html>
<html lang="en">
<head>
<meta charset="utf-8">
<title>Grant T. Vellimore — Business Card</title>
<link rel="stylesheet" href="https://fonts.googleapis.com/css2?family=Cinzel:wght@400;500;600&display=swap">
<style>
  :root {
    --bg: #e3e3e3;
    --paper: #ffffff;
    --teal-dark: #2d6a62;
    --teal-bright: #0f8b79;
    --teal-text: #138a78;
    --ink: #2a2a2a;
    --shadow: rgba(0, 0, 0, 0.22);
  }
  * { box-sizing: border-box; margin: 0; padding: 0; }
  html, body {
    width: 1200px; height: 1000px; overflow: hidden;
    background: var(--bg);
    font-family: "Cinzel", "Times New Roman", serif;
    color: var(--ink);
  }
  .card {
    position: absolute; left: 250px;
    width: 700px; height: 400px;
    background: var(--paper);
    box-shadow: 0 6px 18px var(--shadow);
    overflow: hidden;
  }
  /* Reverse side */
  .card--reverse { top: 70px; }
  .reverse__title-band {
    position: absolute; left: 0; top: 0; width: 100%; height: 190px;
    background: var(--teal-dark);
    display: flex; flex-direction: column; align-items: center; justify-content: center;
    color: var(--paper); text-align: center;
  }
  .book-title__line { font-size: 36px; font-weight: 500; letter-spacing: 2px; line-height: 1.05; }
  .book-title__or { font-size: 13px; letter-spacing: 1px; line-height: 1.2; }
  .reverse__quote {
    position: absolute; left: 30px; right: 30px; top: 215px;
    text-align: center; font-size: 13.5px; line-height: 1.55; color: var(--ink);
  }
  .reverse__footer-band {
    position: absolute; left: 0; bottom: 0; width: 100%; height: 24px;
    background: var(--teal-bright);
  }
  /* Front side */
  .card--front { top: 530px; }
  .front__name {
    position: absolute; left: 55px; top: 45px;
    font-size: 40px; font-weight: 500; color: var(--teal-text); letter-spacing: 1px;
  }
  .peer-review { position: absolute; left: 55px; top: 160px; }
  .peer-review__label { font-size: 17px; margin-bottom: 22px; }
  .peer-review__list { list-style: none; font-size: 20px; font-weight: 500; line-height: 1.25; }
  .front__divider {
    position: absolute; left: 385px; top: 145px; width: 2px; height: 185px;
    background: var(--teal-bright);
  }
  .credentials { position: absolute; left: 408px; top: 145px; width: 280px; font-size: 15px; line-height: 1.25; }
  .credentials__block { margin-bottom: 22px; }
  .contact { list-style: none; font-size: 14px; }
  .contact__item { display: flex; align-items: center; gap: 10px; margin-bottom: 10px; }
  .contact__icon { width: 16px; height: 14px; flex: none; }
  .front__footer { position: absolute; left: 0; bottom: 0; width: 700px; height: 50px; }
</style>
</head>
<body>
  <section class="card card--reverse">
    <div class="reverse__title-band">
      <div class="book-title__line">Moral Roots</div>
      <div class="book-title__or">or</div>
      <div class="book-title__line">Civic Roots</div>
    </div>
    <p class="reverse__quote">
      In the distant future I see open fields for far more important researches.<br>
      Psychology will be based on a new foundation,<br>
      that of the necessary squire Kent of each mental power by gradation.<br>
      Light will be thrown on the origin of man and his history. —Edmund Farrow
    </p>
    <div class="reverse__footer-band"></div>
  </section>

  <section class="card card--front">
    <h1 class="front__name">Grant T. Vellimore, Ph.D.</h1>

    <div class="peer-review">
      <p class="peer-review__label">Peer review by:</p>
      <ul class="peer-review__list">
        <li>Harwick Scholarly Press</li>
        <li>Marten Books</li>
        <li>R. J. Fallow Co.</li>
        <li>Peter Quade &amp; Sons</li>
      </ul>
    </div>

    <div class="front__divider"></div>

    <div class="credentials">
      <p class="credentials__block">Evolutionary Scientist<br>Historian</p>
      <p class="credentials__block">Academic Consultant,<br>Ellsworth Academic Press</p>
      <ul class="contact">
        <li class="contact__item">
          <svg class="contact__icon" viewBox="0 0 16 14" aria-hidden="true">
            <path d="M1 4 Q8 -1 15 4 L13 6 L11 4.5 L5 4.5 L3 6 Z" fill="var(--teal-bright)"/>
            <rect x="3" y="7" width="10" height="6" rx="1" fill="var(--teal-bright)"/>
            <circle cx="8" cy="10" r="1.6" fill="var(--paper)"/>
          </svg>
          <span>(555) 214-0873</span>
        </li>
        <li class="contact__item">
          <svg class="contact__icon" viewBox="0 0 16 12" aria-hidden="true">
            <rect x="0.5" y="0.5" width="15" height="11" fill="var(--teal-bright)"/>
            <path d="M1 1 L8 7 L15 1" fill="none" stroke="var(--paper)" stroke-width="1.3"/>
          </svg>
          <span>grantvell@mailbrook.net</span>
        </li>
      </ul>
    </div>

    <svg class="front__footer" viewBox="0 0 700 50" aria-hidden="true">
      <polygon points="0,24 288,24 304,50 0,50" fill="var(--teal-bright)"/>
      <polygon points="296,8 700,8 700,50 320,50" fill="var(--teal-dark)"/>
    </svg>
  </section>
</body>
</html>
```